Everything fresh, everything new

When I take over the practice, I would like to breathe new life into the practice. I want a business card design that catches the eye and brings a breath of fresh air

```html
<!DOCTYPE html>
<html lang="de">
<head>
<meta charset="utf-8">
<title>Vitalwerk – Visitenkarte</title>
<link rel="stylesheet" href="https://fonts.googleapis.com/css2?family=Poppins:wght@400;500&display=swap">
<style>
  :root {
    --green: #76bf3a;
    --ink: #3f4042;
    --card-dark: #4a4b4d;
    --paper: #ffffff;
    --stage: #2b2c2e;
    --stripe-grey: #8a8b8d;
  }
  * { box-sizing: border-box; margin: 0; padding: 0; }
  html, body {
    width: 1200px; height: 900px; overflow: hidden;
    background: var(--stage);
    font-family: "Poppins", sans-serif;
  }
  .stage {
    width: 1200px; height: 900px;
    display: flex; flex-direction: column; align-items: center; justify-content: center;
    gap: 40px;
  }
  .card {
    position: relative; width: 700px; height: 400px; overflow: hidden;
    box-shadow: 0 12px 30px rgba(0,0,0,.35);
  }

  /* Brand name set as plain type */
  .brand { display: flex; flex-direction: column; align-items: center; text-align: center; }
  .brand__name { font-weight: 500; line-height: 1; letter-spacing: -0.5px; }
  .brand__tag { font-weight: 400; margin-top: 8px; letter-spacing: 0.3px; }

  /* Front */
  .card--front { background: var(--paper); color: var(--ink); }
  .card--front .brand { position: absolute; left: 330px; top: 62px; width: 300px; }
  .card--front .brand__name { font-size: 40px; color: var(--ink); }
  .card--front .brand__tag { font-size: 12px; color: var(--ink); }

  .divider {
    position: absolute; left: 40px; top: 160px; width: 570px; height: 2px;
    background: var(--green);
  }

  .person { position: absolute; left: 40px; top: 190px; }
  .person__name {
    font-size: 30px; font-weight: 500; color: var(--green);
    text-transform: uppercase; letter-spacing: -0.5px; line-height: 1.1;
  }
  .person__role { font-size: 24px; color: var(--ink); margin-top: 2px; }

  .contact { position: absolute; left: 360px; top: 196px; list-style: none; }
  .contact li {
    display: flex; align-items: center; gap: 12px;
    font-size: 19px; line-height: 1; margin-bottom: 13px; color: var(--ink);
  }
  .contact svg { width: 18px; height: 18px; flex: none; }

  .edge-green {
    position: absolute; left: 0; bottom: 0; width: 385px; height: 16px; background: var(--green);
  }
  .edge-dark {
    position: absolute; left: 385px; bottom: 4px; right: 0; height: 6px; background: var(--ink);
  }
  .edge-grey {
    position: absolute; left: 385px; bottom: 0; right: 0; height: 3px; background: var(--stripe-grey);
  }

  /* Back */
  .card--back { background: var(--card-dark); display: flex; align-items: center; justify-content: center; }
  .card--back .brand__name { font-size: 58px; color: var(--paper); }
  .card--back .brand__tag { font-size: 15px; color: var(--paper); }
</style>
</head>
<body>
<main class="stage">
  <section class="card card--front" aria-label="Vorderseite">
    <div class="brand">
      <span class="brand__name">Vitalwerk</span>
      <span class="brand__tag">Aktiv im Alltag</span>
    </div>
    <div class="divider"></div>
    <div class="person">
      <p class="person__name">Lukas Berger</p>
      <p class="person__role">Founder/CEO</p>
    </div>
    <ul class="contact">
      <li>
        <svg viewBox="0 0 20 20"><circle cx="10" cy="10" r="10" fill="var(--green)"/><path d="M7 5.5l2 2-1.2 1.3a6 6 0 003.4 3.4L12.5 11l2 2-1.4 1.5C9.5 14.3 5.7 10.5 5.5 6.9z" fill="#fff"/></svg>
        012 345 6789
      </li>
      <li>
        <svg viewBox="0 0 20 20"><circle cx="10" cy="10" r="10" fill="var(--green)"/><rect x="6" y="7" width="8" height="7" rx="1" fill="#fff"/><rect x="7.5" y="4.5" width="5" height="3" fill="#fff"/></svg>
        098 765 4321
      </li>
      <li>
        <svg viewBox="0 0 20 20"><circle cx="10" cy="10" r="10" fill="var(--green)"/><rect x="5" y="6.5" width="10" height="7" rx="1" fill="#fff"/><path d="M5.5 7l4.5 3.5L14.5 7" stroke="var(--green)" stroke-width="1.2" fill="none"/></svg>
        info@vitalwerk.com
      </li>
      <li>
        <svg viewBox="0 0 20 20"><circle cx="10" cy="10" r="10" fill="var(--green)"/><circle cx="10" cy="10" r="5" stroke="#fff" stroke-width="1.3" fill="none"/><path d="M5 10h10M10 5c-2.5 3-2.5 7 0 10M10 5c2.5 3 2.5 7 0 10" stroke="#fff" stroke-width="1.1" fill="none"/></svg>
        www.vitalwerk.com
      </li>
    </ul>
    <div class="edge-green"></div>
    <div class="edge-dark"></div>
    <div class="edge-grey"></div>
  </section>

  <section class="card card--back" aria-label="Rückseite">
    <div class="brand">
      <span class="brand__name">Vitalwerk</span>
      <span class="brand__tag">Aktiv im Alltag</span>
    </div>
  </section>
</main>
</body>
</html>
```